Funky Modern Flyer A5 or Postcard size

Hi, I am looking at a one small flyer (A5 or postcard size) that I can put both on my website on the front page (ie so png) and also send out if necessary.

It has to be modern, funky and hip. My brand is professional / Corporate so it also has to fit in with that brand.

There are 6 attachments:
Example 1 - FernaPeak - I like this look, clean, modern, funky and says it all.
Example 2 - FernPeak - again another look I like, simple, explanatory
Example 4 - Brightstall Bazaar - font is cool on this one but background not so much too much going on but I like the font
Example 5 - Example 4 - Brightstall Bazaar - font is cool on this one but background not so much too much going on but I like the font
5 is my logo
Example 6 is something I found on the web this morning which is effective.

It is for a Mentoring and Training program I run called: HIGHSTRIDE

What is to be included is the following:
The name: Highstride
Somewhere: Training, Mentoring
My Logo (see attached two options) you can choose which colour suits and I have the source file should you need it
My website and email: www.miriambaskell.example / miriam@miriambaskell.example

This wording: This is one of our highest in-demand programs and is based on a background and proven track record by Miriam in accelerating sales organisations and their people into stand out high performers. **(NOTE this wording in this paragraph may change and I am open to you changing if you think you can make it more effective!)

Colours: white, black and gold (those are our website colours).

I'd like the Highstride to really stand out.... I have included two fonts that I really like that I got off Brightstall Bazaar. However, feel free to suggest other fonts that you think cool or funky!
Updates

Hi everyone, just to add a note to the brief, I am not overly keen on pictures that are really busy. I only like a picture that is minimal and effective. The examples from Brightstall Bazaar was more for the Font Style not so much the pictures in the background. The pictures can take away from a design unless done really minimally.....hope this makes sense. Miriam Added Wednesday, March 15, 2017

Target Market(s)

My target Market is Corporates but I want a Funky Modern look as a lot of people in Corporates are Millennials as well which is part of my target market

Industry/Entity Type

Information Technology

Requirements
Must have
• What is to be included is the following:
• The name: Highstride
• Somewhere: Training, Mentoring
• My Logo (see attached two options) you can choose which colour suits and I have the source file should you need it
• My website and email: www.miriambaskell.example / miriam@miriambaskell.example
• This wording: This is one of our highest in-demand programs and is based on a background and proven track record in high performance and accelerating sales organisations and their people into stand out high performers. (**NOTE this wording may change when final design is picked to be changed as still working in it***)
• Colours: white, black and gold (those are our website colours).
• I'd like the Highstride to really stand out.... I have included two fonts that I really like that I got off Brightstall Bazaar. However, feel free to suggest other fonts that you think cool or funky! NOTE: The pictures I have attached is mainly for the FONTS not for the background pictures. I am not that keen on background pictures as it can take away from the font - unless it is minimal
Should not have
• Too many different colours, I like slick, modern, clean. White, gold and black preferred as this is our website colour.
• NOTE: The pictures from Brightstall Bazaar I have attached are mainly for the FONTS not for the background pictures. I am not hugely keen on background pictures as it can take away from the font/message - unless the pictures are minimal but effective.

```html
<!DOCTYPE html>
<html lang="en">
<head>
<meta charset="utf-8">
<title>Highstride – Training &amp; Mentoring</title>
<link rel="stylesheet" href="https://fonts.googleapis.com/css2?family=Questrial&family=Caveat+Brush&family=Noto+Serif&display=swap">
<style>
  :root {
    --backdrop: #2b1c14;
    --ink: #060606;
    --gold: #d4ac3a;
    --white: #ffffff;
    --body-grey: #d9d9d9;
    --map-tone: #5c6a6c;
    --band: #141414;
  }
  html, body {
    margin: 0;
    padding: 0;
    width: 1200px;
    height: 1200px;
    overflow: hidden;
    background: var(--backdrop);
  }
  .flyer {
    position: absolute;
    left: 167px;
    top: 40px;
    width: 866px;
    height: 1120px;
    background: var(--ink);
    overflow: hidden;
  }
  .hero-photo {
    position: absolute;
    inset: 0 0 300px 0;
    background:
      linear-gradient(to bottom, rgba(6,6,6,0) 55%, var(--ink) 100%),
      radial-gradient(ellipse 70% 60% at 50% 40%, #7e8b8c 0%, var(--map-tone) 35%, #2c3334 70%, var(--ink) 100%);
  }
  .brand-mark {
    position: absolute;
    top: 118px;
    left: 0;
    width: 100%;
    display: flex;
    justify-content: center;
    align-items: center;
    gap: 18px;
    font-family: "Questrial", sans-serif;
    font-size: 48px;
    color: var(--gold);
  }
  .brand-mark-square {
    width: 22px;
    height: 22px;
    background: var(--gold);
  }
  .owner-name {
    position: absolute;
    top: 286px;
    width: 100%;
    text-align: center;
    font-family: "Questrial", sans-serif;
    font-size: 58px;
    letter-spacing: 3px;
    color: var(--gold);
  }
  .swoosh {
    position: absolute;
    inset: 0;
  }
  .headline {
    position: absolute;
    left: 112px;
    top: 660px;
    margin: 0;
    font-family: "Caveat Brush", cursive;
    font-weight: 400;
    font-size: 142px;
    line-height: 1;
    color: var(--white);
    transform: rotate(-8deg);
    transform-origin: left center;
    white-space: nowrap;
  }
  .program-tag {
    position: absolute;
    left: 392px;
    top: 815px;
    font-family: "Caveat Brush", cursive;
    font-size: 48px;
    color: var(--gold);
    transform: rotate(-8deg);
    transform-origin: left center;
    white-space: nowrap;
  }
  .intro {
    position: absolute;
    top: 932px;
    left: 60px;
    right: 60px;
    margin: 0;
    text-align: center;
    font-family: "Noto Serif", serif;
    font-size: 21.5px;
    line-height: 1.42;
    color: var(--body-grey);
  }
  .contact {
    position: absolute;
    top: 1046px;
    left: 64px;
    right: 34px;
    display: flex;
    justify-content: space-between;
    font-family: "Noto Serif", serif;
    font-size: 20px;
    color: var(--gold);
  }
</style>
</head>
<body>
  <main class="flyer">
    <div class="hero-photo" role="img" aria-label="Faded world map behind a row of business professionals with arms crossed and a handshake in the foreground"></div>

    <div class="brand-mark"><span class="brand-mark-square"></span><span>Baskell</span></div>
    <div class="owner-name">MIRIAM BASKELL</div>

    <svg class="swoosh" viewBox="0 0 866 1120" aria-hidden="true">
      <path d="M66 855 C200 930 450 905 650 880 C760 866 810 870 840 900 L812 800 L825 765 C600 780 300 820 66 855 Z" fill="var(--band)"/>
      <path d="M70 850 C200 935 450 915 650 885 C760 870 805 880 838 905" fill="none" stroke="var(--gold)" stroke-width="5" stroke-linecap="round"/>
    </svg>

    <h1 class="headline">HIGHSTRIDE</h1>
    <div class="program-tag">Training &amp; Mentoring</div>

    <p class="intro">This is one of our highest in-demand programs and is based on a background and proven track record by Miriam in accelerating sales organisations and their people into stand out high performers.</p>

    <div class="contact">
      <span class="contact-phone">+6421555018</span>
      <span class="contact-email">miriam@miriambaskell.example</span>
      <span class="contact-web">www.miriambaskell.example</span>
    </div>
  </main>
</body>
</html>
```